BEACON CABS

Taxi card design

Need changes very slow in replying to my messages.

Target Market(s)

Customers

Industry/Entity Type

Taxi

Contact Information for Business Card

See previous design

Font styles to use
Sans Serif

Colors
A7469A
B969AE
D3A5CF
EDDBEB
F8F0F9
6B429C
8869AF
B7A5CE
E3DAEB
F3F0F8

Requirements
Nice to have
• We are in the business of looking after people, not just driving vehicles front
Should not have
• Front number 01632 480 480 needs to big big

```html
<!DOCTYPE html>
<html lang="en">
<head>
<meta charset="utf-8">
<title>Beacon Cabs – Business Card</title>
<link href="https://fonts.googleapis.com/css2?family=Saira+Semi+Condensed:wght@500;600;700&display=swap" rel="stylesheet">
<style>
  :root {
    --plum: #A7469A;
    --violet: #6B429C;
    --ink: #111111;
    --white: #ffffff;
    --backdrop: #cccccc;
  }
  html, body {
    margin: 0;
    width: 1096px;
    height: 1200px;
    overflow: hidden;
    background: var(--backdrop);
    font-family: "Saira Semi Condensed", Arial, sans-serif;
  }
  .stage {
    position: relative;
    width: 1220px;
    height: 1336px;
    transform: scale(0.8984);
    transform-origin: 0 0;
  }
  .card {
    position: absolute;
    left: 85px;
    width: 1050px;
    height: 600px;
    overflow: hidden;
  }
  .card--front { top: 51px; background: var(--white); color: var(--ink); }
  .card--back {
    top: 685px;
    background: linear-gradient(180deg, var(--plum), var(--violet));
    color: var(--white);
  }
  .abs { position: absolute; margin: 0; white-space: nowrap; }

  .brand-name { left: 38px; top: 82px; font-size: 66px; font-weight: 700; line-height: 1; letter-spacing: 1px; }
  .established { left: 60px; top: 152px; font-size: 23px; font-weight: 600; }
  .hours { left: 65px; top: 184px; font-size: 40px; font-weight: 600; line-height: 1.1; }

  .services {
    right: 0; top: 0;
    width: 447px; height: 183px;
    border-bottom-left-radius: 80px;
    background: linear-gradient(180deg, var(--plum), var(--violet));
    color: var(--white);
    display: flex; flex-direction: column; justify-content: center; align-items: center;
    font-size: 35px; font-weight: 600; line-height: 48px;
  }

  .phone { display: flex; align-items: center; gap: 14px; font-weight: 600; }
  .phone svg { display: block; }
  .phone--main { left: 322px; top: 255px; font-size: 60px; gap: 16px; }
  .phone--line { top: 344px; font-size: 36px; gap: 12px; }
  .phone--a { left: 42px; }
  .phone--b { left: 389px; }
  .phone--c { left: 746px; }

  .divider { left: 36px; top: 398px; width: 979px; height: 3px; background: var(--violet); }

  .info { top: 416px; font-size: 29px; font-weight: 600; line-height: 40.5px; }
  .info--contact { left: 38px; }
  .info--address { left: 695px; }

  .back-name { left: 0; right: 0; top: 210px; text-align: center; font-size: 104px; font-weight: 700; letter-spacing: 2px; line-height: 1; }
  .phone--back { left: 281px; top: 405px; font-size: 70px; gap: 18px; }
</style>
</head>
<body>
<div class="stage">

  <section class="card card--front">
    <p class="abs brand-name">BEACON CABS</p>
    <p class="abs established">Established since 1986</p>
    <p class="abs hours">24/7 Service</p>

    <div class="abs services">
      <span>AIRPORT TRANSFERS</span>
      <span>MINIBUSES</span>
      <span>SCHOOL TRANSPORT</span>
    </div>

    <div class="abs phone phone--main">
      <svg width="50" height="50" viewBox="0 0 50 50" aria-hidden="true">
        <rect width="50" height="50" rx="6" fill="#111"/>
        <path d="M17 11c2-1 3 0 4 2l2 5c1 2 0 3-1 4l-2 1c1 4 4 7 8 9l1-2c1-1 2-2 4-1l5 2c2 1 3 2 2 4l-1 3c-1 2-3 3-6 2-9-3-16-10-19-19-1-3 0-5 3-6z" fill="#fff"/>
      </svg>
      <span>01632 480 480</span>
    </div>

    <div class="abs phone phone--line phone--a">
      <svg width="34" height="34" viewBox="0 0 50 50" aria-hidden="true">
        <rect width="50" height="50" rx="6" fill="#111"/>
        <path d="M17 11c2-1 3 0 4 2l2 5c1 2 0 3-1 4l-2 1c1 4 4 7 8 9l1-2c1-1 2-2 4-1l5 2c2 1 3 2 2 4l-1 3c-1 2-3 3-6 2-9-3-16-10-19-19-1-3 0-5 3-6z" fill="#fff"/>
      </svg>
      <span>01632 79 66 66</span>
    </div>
    <div class="abs phone phone--line phone--b">
      <svg width="34" height="34" viewBox="0 0 50 50" aria-hidden="true">
        <rect width="50" height="50" rx="6" fill="#111"/>
        <path d="M17 11c2-1 3 0 4 2l2 5c1 2 0 3-1 4l-2 1c1 4 4 7 8 9l1-2c1-1 2-2 4-1l5 2c2 1 3 2 2 4l-1 3c-1 2-3 3-6 2-9-3-16-10-19-19-1-3 0-5 3-6z" fill="#fff"/>
      </svg>
      <span>01632 20 20 20</span>
    </div>
    <div class="abs phone phone--line phone--c">
      <svg width="34" height="34" viewBox="0 0 50 50" aria-hidden="true">
        <rect width="50" height="50" rx="6" fill="#111"/>
        <path d="M17 11c2-1 3 0 4 2l2 5c1 2 0 3-1 4l-2 1c1 4 4 7 8 9l1-2c1-1 2-2 4-1l5 2c2 1 3 2 2 4l-1 3c-1 2-3 3-6 2-9-3-16-10-19-19-1-3 0-5 3-6z" fill="#fff"/>
      </svg>
      <span>01632 79 88 11</span>
    </div>

    <div class="abs divider"></div>

    <div class="abs info info--contact">
      Freephone: 0800 555 0 123<br>
      Email: bookings@beaconcabs.co.uk<br>
      Website: www.beaconcabs.co.uk
    </div>
    <div class="abs info info--address">
      Mill Lane Yard<br>
      Harbour St<br>
      Ashford Vale<br>
      AV12 3QP
    </div>
  </section>

  <section class="card card--back">
    <p class="abs back-name">BEACON CABS</p>
    <div class="abs phone phone--back">
      <svg width="60" height="60" viewBox="0 0 50 50" aria-hidden="true">
        <rect width="50" height="50" rx="5" fill="#fff"/>
        <path d="M17 11c2-1 3 0 4 2l2 5c1 2 0 3-1 4l-2 1c1 4 4 7 8 9l1-2c1-1 2-2 4-1l5 2c2 1 3 2 2 4l-1 3c-1 2-3 3-6 2-9-3-16-10-19-19-1-3 0-5 3-6z" fill="#8a3f9a"/>
      </svg>
      <span>01632 480 480</span>
    </div>
  </section>

</div>
</body>
</html>
```